Design a 1-page brochure with our "The Harbinger Pathway" illustrated.

i have included my logo, an outline of the text and name of each step, and a quick sketch of generally how i would like the image to look. But please make it look sexy.

Each step should include the subtext as shown on the pdf attached. i.e. The first part of the image (far left) is "Problems", under that should list : 1. Poor Expectations; 2. Poor Communication... and so on for all the steps included.

I have also included a previous brochure that shows our branding and style.

Target Market(s)

Restaurant, Retail, Commercial

Industry/Entity Type

Construction Management

Font styles to use
Sans Serif

Colors
EB3D1F
EC4F4E
F09395
F8D3D4
FCEDEE

Requirements
Must have
• Our logo. Title of graphic: The Harbinger Pathway, our website and IG. www.quorvanbuildco.example. @quorvanbuildco

```html
<!DOCTYPE html>
<html lang="en">
<head>
<meta charset="utf-8">
<title>The Harbinger Pathway — Quorvan Build Co</title>
<link rel="stylesheet" href="https://fonts.googleapis.com/css2?family=Montserrat:wght@300;400;600;700;800&display=swap">
<style>
  :root {
    --ink: #111111;
    --paper: #ffffff;
    --brand-red: #b5161f;
    --brand-red-light: #d41f27;
    --step-organize: #a3a3a3;
    --step-execute: #856b05;
    --step-manage: #044593;
    --step-complete: #218a35;
    --rule-grey: #b9b9b9;
    --scene-dark: #1d2423;
    --scene-mid: #38433d;
    --scene-warm: #5a4a38;
  }
  * { margin: 0; padding: 0; box-sizing: border-box; }
  html, body { width: 1200px; height: 848px; overflow: hidden; background: var(--paper); }
  body { font-family: "Montserrat", sans-serif; color: var(--ink); }

  .brochure { position: relative; width: 1200px; height: 848px; overflow: hidden; background: var(--paper); }

  .backdrop { position: absolute; inset: 0; width: 1200px; height: 848px; }

  .brand { position: absolute; left: 51px; top: 58px; width: 258px; text-align: center; }
  .brand-mark { width: 132px; height: 132px; margin: 0 auto 48px; background: var(--brand-red); }
  .brand-name { font-weight: 800; font-size: 19.5px; letter-spacing: 0.5px; color: var(--ink); white-space: nowrap; }

  .title {
    position: absolute; left: 332px; top: 80px;
    font-weight: 800; font-size: 41px; letter-spacing: 0.5px;
    font-variant: small-caps; white-space: nowrap; color: var(--ink);
  }

  .column-heading {
    position: absolute; font-weight: 600; font-size: 20px; color: var(--paper);
    letter-spacing: 0.2px; white-space: nowrap;
  }
  .problems-heading { left: 61px; top: 538px; }
  .dream-heading { left: 870px; top: 271px; }

  .point-list { list-style: none; position: absolute; color: var(--paper); }
  .point-list li {
    position: absolute; white-space: nowrap; font-weight: 600; font-size: 20px;
    font-variant: small-caps; letter-spacing: 0.4px;
  }
  .problems-list { left: 39px; top: 578px; }
  .problems-list li:nth-child(1) { top: 0; }
  .problems-list li:nth-child(2) { top: 31px; }
  .problems-list li:nth-child(3) { top: 63px; }
  .problems-list li:nth-child(4) { top: 94px; }
  .problems-list li:nth-child(5) { top: 125px; }

  .dream-list { left: 0; top: 313px; }
  .dream-list li:nth-child(1) { left: 849px; top: 0; }
  .dream-list li:nth-child(2) { left: 844px; top: 31px; }
  .dream-list li:nth-child(3) { left: 839px; top: 63px; }
  .dream-list li:nth-child(4) { left: 834px; top: 94px; }

  .step-label { font-family: "Montserrat", sans-serif; font-weight: 700; font-size: 20.5px; fill: var(--paper); letter-spacing: 0.5px; }

  .social-handle {
    position: absolute; left: 604px; top: 782px;
    font-weight: 400; font-size: 18px; color: var(--paper); white-space: nowrap;
  }
  .web-link {
    position: absolute; left: 820px; top: 781px;
    font-weight: 400; font-size: 21px; color: var(--paper); white-space: nowrap;
  }
</style>
</head>
<body>
<main class="brochure">
  <svg class="backdrop" viewBox="0 0 1200 848">
    <defs>
      <linearGradient id="scene-tone" x1="0" y1="0" x2="1" y2="1">
        <stop offset="0" stop-color="#38433d"/>
        <stop offset="0.5" stop-color="#1d2423"/>
        <stop offset="1" stop-color="#5a4a38"/>
      </linearGradient>
      <linearGradient id="band-tone" x1="0" y1="0" x2="1" y2="0">
        <stop offset="0" stop-color="#b5161f"/>
        <stop offset="1" stop-color="#d41f27"/>
      </linearGradient>
    </defs>

    <polygon class="scene-photo" role="img"
      aria-label="Evening aerial rendering of a completed mixed-use development with lit plazas, sports fields and a riverside stage"
      points="0,499 845,206 1200,238 1200,848 0,848" fill="url(#scene-tone)"/>

    <polygon class="roof-band" points="0,486 845,181 1200,206 1200,238 845,206 0,499" fill="var(--brand-red)"/>

    <line class="problems-rule" x1="51" y1="566" x2="300" y2="566" stroke="var(--rule-grey)" stroke-width="1.5"/>
    <line class="dream-rule" x1="835" y1="302" x2="1105" y2="302" stroke="var(--step-complete)" stroke-width="2"/>

    <g class="pathway">
      <polygon class="step step-organize" points="300,566 443,495 443,680 363,680" fill="var(--step-organize)"/>
      <polygon class="step step-execute" points="443,495 558,439 558,680 443,680" fill="var(--step-execute)"/>
      <polygon class="step step-manage" points="558,439 686,375 686,680 558,680" fill="var(--step-manage)"/>
      <polygon class="step step-complete" points="686,375 835,302 767,680 686,680" fill="var(--step-complete)"/>

      <text class="step-label" transform="translate(399,663) rotate(-90)">ORGANIZE</text>
      <text class="step-label" transform="translate(511,633) rotate(-90)">EXECUTE</text>
      <text class="step-label" transform="translate(629,599) rotate(-90)">MANAGE</text>
      <text class="step-label" transform="translate(746,564) rotate(-90)">COMPLETE</text>
    </g>

    <polygon class="contact-band" points="585,767 1200,767 1200,822 548,822" fill="url(#band-tone)"/>
    <g class="globe-icon" fill="none" stroke="var(--paper)" stroke-width="1.3">
      <circle cx="786" cy="795" r="13"/>
      <ellipse cx="786" cy="795" rx="6" ry="13"/>
      <line x1="773" y1="795" x2="799" y2="795"/>
      <line x1="775" y1="788" x2="797" y2="788"/>
      <line x1="775" y1="802" x2="797" y2="802"/>
      <line x1="786" y1="782" x2="786" y2="808"/>
    </g>
  </svg>

  <div class="brand">
    <div class="brand-mark"></div>
    <div class="brand-name">QUORVAN BUILD CO</div>
  </div>

  <h1 class="title">The Harbinger Pathway</h1>

  <h2 class="column-heading problems-heading">COMMON PROBLEMS</h2>
  <ol class="point-list problems-list">
    <li>1. Poor expectations</li>
    <li>2. Poor communication</li>
    <li>3. No journey to success</li>
    <li>4. No trust</li>
    <li>5. No accountability</li>
  </ol>

  <h2 class="column-heading dream-heading">DREAM POSSIBILITY</h2>
  <ol class="point-list dream-list">
    <li>1. Project synergy</li>
    <li>2. Excellent communication</li>
    <li>3. Clear project visibility</li>
    <li>4. Proud final product</li>
  </ol>

  <span class="social-handle">@quorvanbuildco</span>
  <a class="web-link">www.quorvanbuildco.example</a>
</main>
</body>
</html>
```